KB Sports & Remedial Massage needs a new logo & business card design

The design is for my Sports and remedial massage business. My business is aimed at everyone who has a muscle ache or injury so not just sports related. I need a design which is sharp, clear and professional. No greens, or pastel colours or floral/girly designs. Perhaps just a Navy background and white text or other way around or perhaps grey. I want to make it clear that I treat everyone and not just sporty people.

Target Market(s)

People with muscle aches or sports injuries

Industry/Entity Type

Health And Wellness

Contact Information for Business Card

It needs to also include the following:
Name: Megan Hartwell
Mobile No: 07493 215 648
Email: meganhartwell@parcelnet.example
Qualifications: Dip SM, Dip SRM

Logo Text

KB Sports & Remedial Massage

Font styles to use
Serif
Other font styles liked:
• Tahoma, Verdana

Colors
5c5c5c
7f7f7f
9d9d9d
0255a3
3176b5
85abd2

Requirements
Must have
• I was thinking of a few simple people figures at the bottom of the card to highlight this i.e. a gardener, musician mixed in with a cyclist and tennis player.
Should not have
• Anything which indicates beauty therapy or relaxing. I am there to get rid of aches and pains and often to give rehab to certain injuries.

```html
<!DOCTYPE html>
<html lang="en">
<head>
<meta charset="utf-8">
<title>Megan Hartwell – Business Card</title>
<link href="https://fonts.googleapis.com/css2?family=PT+Sans:wght@400;700&family=PT+Sans+Narrow:wght@400&display=swap" rel="stylesheet">
<style>
  :root {
    --page-bg: #ffffff;
    --wood-light: #f3c98f;
    --wood-mid: #d99247;
    --wood-dark: #a95c1c;
    --panel-veil: rgba(255, 255, 255, 0.36);
    --contact-band: rgba(93, 125, 186, 0.86);
    --name-blue: #1f75c1;
    --qual-grey: #3a3a3a;
    --contact-text: #ffffff;
    --icon-light: #ffffff;
    --icon-dark: #b9bcc2;
    --icon-glyph: #2a2a2a;
    --figure-blue: #2f78bd;
    --figure-grey: #c3c5ca;
  }
  * { margin: 0; padding: 0; box-sizing: border-box; }
  html, body {
    width: 1200px;
    height: 1000px;
    overflow: hidden;
    background: var(--page-bg);
    font-family: "PT Sans", Tahoma, sans-serif;
  }
  .card {
    position: absolute;
    left: 72px;
    top: 148px;
    width: 1070px;
    height: 692px;
    overflow: hidden;
  }
  .card__texture {
    position: absolute;
    inset: 0;
    background: radial-gradient(ellipse 60% 65% at 48% 38%, var(--wood-light) 0%, var(--wood-mid) 55%, var(--wood-dark) 100%);
  }
  .card__panel {
    position: absolute;
    left: 179px;
    top: 105px;
    width: 668px;
    height: 340px;
    background: var(--panel-veil);
  }
  .brand-figure {
    position: absolute;
    left: 179px;
    top: 150px;
    width: 258px;
    height: 282px;
    border-radius: 45% 50% 40% 55%;
    background: radial-gradient(ellipse at 55% 55%, var(--figure-blue) 0%, var(--figure-blue) 40%, var(--figure-grey) 75%, rgba(195,197,202,0) 100%);
    opacity: 0.85;
  }
  .identity {
    position: absolute;
    left: 440px;
    top: 236px;
    width: 380px;
    text-align: center;
  }
  .identity__name {
    font-size: 51px;
    font-weight: 400;
    color: var(--name-blue);
    line-height: 1;
    white-space: nowrap;
  }
  .identity__quals {
    margin-top: 10px;
    font-size: 35px;
    color: var(--qual-grey);
    line-height: 1;
  }
  .contact-band {
    position: absolute;
    left: 179px;
    top: 445px;
    width: 668px;
    height: 93px;
    background: var(--contact-band);
  }
  .contact-item {
    position: absolute;
    top: 0;
    height: 93px;
    display: flex;
    align-items: center;
    color: var(--contact-text);
    white-space: nowrap;
  }
  .contact-item--phone { left: 34px; font-size: 21px; letter-spacing: 1px; }
  .contact-item--email {
    left: 289px;
    font-family: "PT Sans Narrow", "PT Sans", sans-serif;
    font-size: 24px;
  }
  .contact-item__icon {
    width: 44px;
    height: 44px;
    margin-right: 14px;
    flex: none;
  }
  .contact-item--email .contact-item__icon { margin-right: 16px; }
</style>
</head>
<body>
  <div class="card">
    <div class="card__texture" role="img" aria-label="Warm wooden plank texture background"></div>
    <div class="card__panel"></div>
    <div class="brand-figure" role="img" aria-label="Silhouette of a tennis player serving, framed by a grey swoosh"></div>

    <div class="identity">
      <h1 class="identity__name">Megan Hartwell</h1>
      <p class="identity__quals">Dip SM, Dip SRM</p>
    </div>

    <div class="contact-band">
      <div class="contact-item contact-item--phone">
        <svg class="contact-item__icon" viewBox="0 0 44 44" aria-hidden="true">
          <defs>
            <linearGradient id="iconFillA" x1="0" y1="0" x2="0" y2="1">
              <stop offset="0" stop-color="var(--icon-light)"/>
              <stop offset="1" stop-color="var(--icon-dark)"/>
            </linearGradient>
          </defs>
          <circle cx="22" cy="22" r="21" fill="url(#iconFillA)"/>
          <rect x="16.5" y="12" width="11" height="21" rx="2.5" fill="var(--icon-glyph)"/>
          <rect x="18.5" y="15" width="7" height="6" fill="var(--icon-light)"/>
          <circle cx="22" cy="28" r="1.6" fill="var(--icon-light)"/>
        </svg>
        <span>07493 215 648</span>
      </div>
      <div class="contact-item contact-item--email">
        <svg class="contact-item__icon" viewBox="0 0 44 44" aria-hidden="true">
          <defs>
            <linearGradient id="iconFillB" x1="0" y1="0" x2="0" y2="1">
              <stop offset="0" stop-color="var(--icon-light)"/>
              <stop offset="1" stop-color="var(--icon-dark)"/>
            </linearGradient>
          </defs>
          <circle cx="22" cy="22" r="21" fill="url(#iconFillB)"/>
          <rect x="12" y="15" width="20" height="14" fill="none" stroke="var(--icon-glyph)" stroke-width="2"/>
          <polyline points="12,15 22,23 32,15" fill="none" stroke="var(--icon-glyph)" stroke-width="2"/>
        </svg>
        <span>meganhartwell@parcelnet.example</span>
      </div>
    </div>
  </div>
</body>
</html>
```